Tidewell Metrics Group Company Website Design and Coding

We want to redesign our existing website so that it is more visually and functionally appealing to prospective clients and potential job candidates. We would like to keep our current color scheme and implement our current logo as well. We have a high-level idea of website structure that we are thinking of, which is in the attached files. Logo is included as well. The final design would ideally be energy and analytics focused. We will need the new website to be coded as well, please.

Target Market(s)

Energy and utility industry

Industry/Entity Type

Energy/analytics

Coding

Coded - Design and coding required

Number of Pages Required

5+ page

Font styles to use
Sans Serif

Colors
0094D4
00A9DD
6FCCEA
C7EBF8
E9F6FB
F0912C
F2A743
F7CA91
FBE8D2
FDF5EE

Requirements
Must have
• Consistent color scheme- please use the one that we provided. We need an overview, a home page, and our core services. A separate job application page. Logo must be incorporated. We would like e "Meet our Team" page. Please include all of the content that is listed in our attachments.
Nice to have
• Movement
Should not have
• No music, no cartoons/animation, no pictures of a chalkboard

```html
<!DOCTYPE html>
<html lang="en">
<head>
<meta charset="utf-8">
<title>Tidewell Metrics Group</title>
<link href="https://fonts.googleapis.com/css2?family=Nunito:wght@400;600;700&family=Open+Sans:wght@700&display=swap" rel="stylesheet">
<style>
:root{
  --blue:#0094D4;
  --blue-2:#00A9DD;
  --blue-soft:#C7EBF8;
  --orange:#F0912C;
  --orange-2:#F2A743;
  --ink:#4a5170;
  --muted:#9aa0b3;
  --tint:#f5f9fc;
  --white:#ffffff;
}
*{box-sizing:border-box;margin:0;padding:0}
html,body{width:1200px;height:2216px;overflow:hidden;background:var(--white)}
body{font-family:"Nunito",sans-serif;color:var(--ink);position:relative}
.page{position:absolute;left:139px;top:86px;width:918px;height:2028px;background:var(--white);box-shadow:18px 22px 40px rgba(0,0,0,.12)}
.abs{position:absolute}
.brand{left:184px;top:16px;display:flex;align-items:center;gap:6px;color:var(--blue);font-size:10px;font-weight:600}
.brand-dot{width:14px;height:14px;border-radius:50%;background:var(--blue-soft)}
.nav{left:523px;top:18px;display:flex;gap:11px;font-size:7.5px;color:var(--ink)}
.hero{left:0;top:43px;width:918px;height:425px;background:radial-gradient(circle at 73% 40%,var(--blue-2) 0,var(--blue) 55%);color:var(--white)}
.photo{border-radius:3px;box-shadow:0 4px 12px rgba(0,0,0,.2)}
.hero-photo{left:201px;top:72px;width:243px;height:162px;background:linear-gradient(135deg,#2c3340,#6a707a 60%,#3a3f48)}
.hero-text{left:473px;top:119px;width:250px;font-size:10.5px;line-height:19px}
.btn-outline{left:650px;top:210px;width:66px;height:20px;border:1.5px solid var(--white);border-radius:3px;font-size:8px;display:flex;align-items:center;justify-content:center}
.mission-title{left:0;top:295px;width:918px;text-align:center;font-size:22px;font-weight:700}
.mission-text{left:294px;top:335px;width:330px;text-align:center;font-size:7px;line-height:13.4px}
.services{left:0;top:468px;width:918px;height:527px;background:var(--tint)}
.section-title{width:918px;left:0;text-align:center;font-size:17px;font-weight:600;color:var(--ink)}
.service{width:169px;text-align:center}
.service-card{left:374px;top:124px;width:169px;height:138px;background:var(--white);border-top:3px solid var(--blue);box-shadow:0 3px 10px rgba(0,0,0,.05)}
.service svg{display:block;margin:0 auto 10px;width:14px;height:14px}
.service h3{font-size:8.5px;font-weight:600;margin-bottom:5px}
.service p{font-size:7px;line-height:11.5px;color:var(--muted)}
.btn-fill{height:24px;border-radius:12px;background:var(--orange-2);color:var(--white);font-size:6.5px;font-weight:700;letter-spacing:.5px;display:flex;align-items:center;justify-content:center}
.feature-title{left:201px;top:1072px;font-size:17px;font-weight:600}
.feature-text{left:201px;top:1100px;width:245px;font-size:7.5px;line-height:15.5px;color:var(--muted)}
.feature-photo{left:473px;top:1072px;width:243px;height:162px;background:linear-gradient(135deg,#c8a57f,#8a6a4d 50%,#3a3a3e)}
.member{top:1343px;width:153px}
.member-photo{width:153px;height:208px}
.member h4{font-size:10.5px;font-weight:600;margin-top:12px}
.member span{font-size:6.5px;color:var(--muted)}
.join{left:0;top:1653px;width:918px;height:228px;background:linear-gradient(100deg,#4f9cf9,#3f5fd6);color:var(--white);text-align:center}
.join h2{position:absolute;left:0;top:62px;width:918px;font-size:20px;font-weight:700}
.join p{position:absolute;left:0;top:99px;width:918px;font-size:8px}
.contact-title{left:201px;top:1938px;font-family:"Open Sans",sans-serif;font-size:24px;font-weight:700;color:#2f3340}
.social{top:1945px;width:18px;height:18px;border-radius:3px;background:var(--orange)}
</style>
</head>
<body>
<div class="page">
  <div class="abs brand"><span class="brand-dot"></span>Tidewell Metrics Group</div>
  <nav class="abs nav"><span>Homepage</span><span>Core Services</span><span>About</span><span>Our Work</span><span>Blog</span><span>Contact Us</span></nav>

  <section class="abs hero">
    <div class="abs photo hero-photo" role="img" aria-label="Photo of hands typing on a laptop showing an analytics dashboard, with a coffee mug"></div>
    <p class="abs hero-text">Tidewell Metrics Group is a consulting company that helps utilities and regulatory agencies navigate the challenges of building a smarter and cleaner energy future.</p>
    <div class="abs btn-outline">Learn More</div>
    <h2 class="abs mission-title">Our Mission</h2>
    <p class="abs mission-text">Tidewell Metrics Group was formed in 2016 to help utilities and regulatory agencies navigate the technical, economic, and policy challenges of building a smarter and cleaner energy future. Through cutting edge research design and analysis methods we provide DSM program administrators with data-driven insights into how various technologies and interventions affect the way homes and businesses use energy.</p>
  </section>

  <section class="abs services">
    <h2 class="abs section-title" style="top:82px">Our Services</h2>
    <div class="abs service-card"></div>
    <div class="abs service" style="left:173px;top:154px">
      <svg viewBox="0 0 14 14" fill="none" stroke="#4a5170"><rect x="3" y="2" width="3" height="10" rx="1.5"/><rect x="8" y="2" width="3" height="10" rx="1.5"/></svg>
      <h3>Predictive Analytics and Forecasting</h3><p>Lorem ipsum dolor sit amet, consectetur adipiscing elit. Vivamus id felis odio. Vestibulum id ligula vitae enim.</p></div>
    <div class="abs service" style="left:374px;top:154px">
      <svg viewBox="0 0 14 14" fill="none" stroke="#4a5170"><rect x="3" y="2" width="8" height="11"/><path d="M5 1.5h4M5 6h4M5 8.5h4M5 11h4"/></svg>
      <h3>T&amp;D Planning</h3><p>Lorem ipsum dolor sit amet, consectetur adipiscing elit. Vivamus id felis odio. Vestibulum id ligula vitae enim.</p></div>
    <div class="abs service" style="left:575px;top:154px">
      <svg viewBox="0 0 14 14" fill="none" stroke="#4a5170"><rect x="2" y="2" width="10" height="7"/><path d="M4 7l2-2 2 1 3-3M7 9v3M5 13l2-1 2 1"/></svg>
      <h3>Evaluation</h3><p>Lorem ipsum dolor sit amet, consectetur adipiscing elit. Vivamus id felis odio. Vestibulum id ligula vitae enim.</p></div>
    <div class="abs service" style="left:173px;top:308px">
      <svg viewBox="0 0 14 14" fill="none" stroke="#4a5170"><ellipse cx="6.5" cy="6" rx="5" ry="4"/><path d="M4 9.5l-1 3 3-2M11 8l1.5 4"/></svg>
      <h3>Pilot &amp; Emerging Tech Support</h3><p>Lorem ipsum dolor sit amet, consectetur adipiscing elit. Vivamus id felis odio. Vestibulum id ligula vitae enim.</p></div>
    <div class="abs service" style="left:374px;top:308px">
      <svg viewBox="0 0 14 14" fill="none" stroke="#4a5170"><path d="M4 3h8v9H3V6M2 2l6 6M5 8h3V5"/></svg>
      <h3>Program Portfolio &amp; Resource Planning</h3><p>Lorem ipsum dolor sit amet, consectetur adipiscing elit. Vivamus id felis odio. Vestibulum id ligula vitae enim.</p></div>
    <div class="abs service" style="left:575px;top:308px">
      <svg viewBox="0 0 14 14" fill="none" stroke="#4a5170"><rect x="2.5" y="1.5" width="9" height="11"/><path d="M4.5 4h5M4.5 6.5h5M4.5 9h5"/></svg>
      <h3>Program Delivery Support</h3><p>Lorem ipsum dolor sit amet, consectetur adipiscing elit. Vivamus id felis odio. Vestibulum id ligula vitae enim.</p></div>
    <div class="abs btn-fill" style="left:419px;top:442px;width:80px">ALL FEATURES</div>
  </section>

  <h2 class="abs feature-title">Program Delivery Support</h2>
  <p class="abs feature-text">Lorem ipsum dolor sit amet, consectetur adipiscing elit, sed do eiusmod tempor incididunt ut labore et dolore magna aliqua. Ut enim ad minim veniam, quis nostrud exercitation ullamco laboris. Duis aute irure dolor in reprehenderit in voluptate velit esse cillum dolore eu fugiat nulla pariatur.</p>
  <div class="abs btn-fill" style="left:201px;top:1210px;width:73px">KNOW MORE</div>
  <div class="abs photo feature-photo" role="img" aria-label="Photo of hands typing on a laptop on a wooden desk"></div>

  <h2 class="abs section-title" style="top:1290px">Our Team</h2>
  <div class="abs member" style="left:201px"><div class="photo member-photo" role="img" aria-label="Portrait of a team member in a navy cardigan" style="background:linear-gradient(160deg,#d9d6d0,#2b3147 70%)"></div><h4>Marcus Olden</h4><span>Manager of HR</span></div>
  <div class="abs member" style="left:382px"><div class="photo member-photo" role="img" aria-label="Portrait of a team member in a grey sweatshirt against a turquoise wall" style="background:linear-gradient(180deg,#5fc4d8,#2aa0c0 60%,#7a9ab8)"></div><h4>Lena Varsk</h4><span>Manager of Finance</span></div>
  <div class="abs member" style="left:564px"><div class="photo member-photo" role="img" aria-label="Portrait of a team member in a black t-shirt looking at a phone" style="background:linear-gradient(160deg,#8a8a8a,#2a2a2c 60%,#5a4a40)"></div><h4>Theo Calder</h4><span>Manager of GA</span></div>

  <section class="abs join">
    <h2>Join with Us</h2>
    <p>Check Job Available</p>
    <div class="abs btn-fill" style="left:428px;top:143px;width:61px">SEE JOBS</div>
  </section>

  <h2 class="abs contact-title">Contact Us</h2>
  <div class="abs social" style="left:502px" role="img" aria-label="Professional network link"></div>
  <div class="abs social" style="left:592px" role="img" aria-label="Microblog link"></div>
  <div class="abs social" style="left:683px" role="img" aria-label="Social network link"></div>
</div>
</body>
</html>
```